www.tlkstaffing.com RE-DESIGN with PressCraft

We need to update our current site to PressCraft and will also need to add several pages. We will not be very picky on the style and elements as long as the colors and logos are the same-- AL INFO ON SITE WILL STAY THE SAME...CURRENT SITE IS VERY OUTDATED.

The project will consist of using the current site as template (all pics, text etc) and then transferring all the info into a more up to date version. We will also need to add the following functions:

1.) Job Listings page of the current openings our recruitment agency is working on (Must be easily edited and changed) and will allow candidate to submit their resumes via a simple email link)

2.) Featured candidate page that highlights one of our current candidates (profile, pic, editable filed so we may paste bio (must be easily edited via word press.

3.) Bio Page of our current Recruiters (4 bios) - Editable so we can make changes

4.) ALL FINAL FILES MUST BE MIGRATED AND UPLOADED VIA THE DESIGNER SO WE CAN MAKE THE SITE.
Updates

Please make the "homepage" a scrolling page that include all the drop down menu categories using the same info on current site. We can edit or scale back the text if needed. Would, like to see new stock photos and photos must scale to fit all the way across screen and also be mobile and tablet friendly.

Target Market(s)

professional

Coding

Coded - Design and coding required

Font styles to use
Sans Serif

Colors
0355a3
ec1f27
000000
1b1b1b

Requirements
Must have
• All the current info on existing site www.tlkstaffing.com
• Would like to have design with scolling home page such as:
• Did you get earlier message about the design I eliminated? I was hoping for site more like this?
• https://www.brightpathhire.com/
• https://www.netmarvel.com.au/lp/seo-analysis/
Nice to have
• Sleek masculine modern feel
Should not have
• No cursive

```html
<!DOCTYPE html>
<html lang="en">
<head>
<meta charset="utf-8">
<title>Lantern Talent Group — Where Recruiters Meet Talent</title>
<link rel="stylesheet" href="https://fonts.googleapis.com/css2?family=Abril+Fatface&family=Open+Sans:wght@300;400;600;700&family=Roboto:wght@400;500&display=swap">
<style>
:root{
  --ink:#1b1b1b;
  --black:#000000;
  --white:#ffffff;
  --salmon:#f07878;
  --salmon-soft:#f38f95;
  --brand-red:#ec1f27;
  --teal:#1e6f88;
  --plum:#4e4862;
  --btn-grey:#5f5f5f;
  --footer-blue:#0a4fa1;
  --footer-rule:#8fb0d8;
  --bar-grey:#6b6b6b;
  --link-purple:#7b62e0;
}
*{box-sizing:border-box;margin:0;padding:0}
html,body{width:1200px;height:2903px;overflow:hidden}
body{position:relative;background:var(--white);font-family:"Open Sans",sans-serif;color:var(--ink)}
.abs{position:absolute}

/* header */
.site-header{left:0;top:0;width:1200px;height:85px;background:var(--white);box-shadow:0 1px 4px rgba(0,0,0,.15);z-index:2}
.brand{left:52px;top:20px;display:flex;align-items:center;gap:10px}
.brand-dot{width:38px;height:38px;border-radius:50%;background:var(--black)}
.brand-name{font-family:"Open Sans",sans-serif;font-weight:600;font-size:30px;color:var(--ink)}
.main-nav{left:352px;top:33px;display:flex;gap:17px;font-size:12.5px;color:#444}
.main-nav span{white-space:nowrap}

/* hero */
.hero{left:0;top:85px;width:1200px;height:554px;background:linear-gradient(100deg,#5a5a5a 0%,#3d3d3f 35%,#505052 60%,#6e6e70 100%)}
.hero-title{left:0;top:150px;width:1200px;text-align:center;font-family:"Abril Fatface",serif;font-size:96px;color:var(--white);line-height:1}
.hero-tag{left:0;top:268px;width:1200px;text-align:center;font-family:"Abril Fatface",serif;font-size:28px;color:var(--white)}
.btn-outline{height:41px;border:2px solid var(--salmon);color:var(--salmon);font-size:15px;display:flex;align-items:center;justify-content:center}
.btn-fill{background:var(--salmon);color:var(--white);font-size:13px;display:flex;align-items:center;justify-content:center}
.scroll-down{left:570px;top:438px;width:60px;height:60px;border-radius:50%;background:#e8e8ee;display:flex;align-items:center;justify-content:center}

/* section titles */
.section-title{left:0;width:1200px;text-align:center;font-size:40px;font-weight:400;color:var(--black)}

/* expertise cards */
.card{width:207px;height:259px}
.card-photo{left:0;top:0;width:207px;height:100px;background:linear-gradient(120deg,#7d8590,#c7ccd2 55%,#5d6470)}
.card-band{left:-9px;top:100px;width:225px;height:33px;background:var(--teal);color:var(--white);font-family:"Roboto",sans-serif;font-weight:500;font-size:12px;display:flex;align-items:center;justify-content:center}
.card-body{left:0;top:133px;width:207px;height:126px;background:var(--plum)}
.card-btn{left:29px;top:40px;width:149px;height:44px;background:var(--btn-grey);color:#e8e8e8;font-family:"Roboto",sans-serif;font-size:13px;display:flex;align-items:center;justify-content:center;box-shadow:0 2px 3px rgba(0,0,0,.3)}

/* about */
.about-photo{left:15px;top:1587px;width:569px;height:381px;background:linear-gradient(110deg,#9a9893,#d8d6d0 45%,#8a857c)}
.about-text{left:615px;top:1597px;width:568px;font-size:17.5px;line-height:29.5px;color:#2a2a2a}
.about-text p{margin-bottom:29px}
.drop-cap{float:left;font-size:138px;line-height:112px;font-weight:300;margin:6px 14px 0 0;color:var(--ink)}
.read-more{left:615px;top:2043px;width:569px;height:42px;border:2px solid var(--salmon);color:var(--salmon);font-size:15px;display:flex;align-items:center;padding-left:30px}

/* call to action band */
.cta-band{left:0;top:2186px;width:1200px;height:297px;background:linear-gradient(100deg,#4c4c4e,#38383a 40%,#4a4a4c 70%,#626264)}
.cta-btn{top:2349px;height:48px;background:linear-gradient(#f5a0a6,var(--salmon-soft));color:var(--white);font-size:17px;display:flex;align-items:center;justify-content:center}
.cta-icon{left:553px;top:2349px;width:49px;height:48px;background:#b8585a;display:flex;align-items:center;justify-content:center}

/* footer */
.site-footer{left:0;top:2483px;width:1200px;height:365px;background:var(--footer-blue);color:var(--white)}
.f-col{top:20px;width:250px}
.f-head{text-align:center;font-size:18px;font-weight:400;padding-bottom:14px;border-bottom:2px solid var(--footer-rule)}
.f-list{margin-top:22px;list-style:none;font-size:15px;line-height:24px}
.contact-lines{margin-top:22px;font-size:14.5px;font-weight:700;line-height:24px}
.contact-lines .gap{height:14px}
.footer-brand{margin-top:30px;display:flex;align-items:center;gap:8px}
.footer-brand .brand-dot{width:34px;height:34px;background:var(--black)}
.footer-brand .brand-name{font-size:30px;color:var(--white);font-weight:600}
.cand-photo{left:0;top:0;width:88px;height:114px;background:linear-gradient(#6b7480,#3f4550)}
.cand-name{left:100px;top:0;font-size:23px;line-height:28px}
.cand-role{left:100px;top:64px;font-size:15px}
.cand-info{left:100px;top:104px;font-size:13px;line-height:19px}
.cand-info div{display:flex;gap:12px;margin-bottom:6px}
.cand-info svg{flex:none;margin-top:3px}

.credit-bar{left:0;top:2848px;width:1200px;height:55px;background:var(--bar-grey);color:#e8e8e8;font-size:14px;display:flex;align-items:center;justify-content:center}
.credit-bar span{color:var(--link-purple)}
</style>
</head>
<body>

<header class="site-header abs">
  <div class="brand abs"><span class="brand-dot"></span><span class="brand-name">Lantern</span></div>
  <nav class="main-nav abs">
    <span>HOME</span><span>ABOUT US</span><span>AREAS OF EXPERTISE ▾</span><span>GUARENTEE</span><span>FAQ</span><span>TESTIMONIALS</span><span>SUBMIT RESUME</span><span>CONTACT US</span>
  </nav>
</header>

<section class="hero abs" role="img" aria-label="Business people shaking hands in an office"></section>
<h1 class="hero-title abs">Lantern Talent Group</h1>
<p class="hero-tag abs">Where Recruiters Meet Tallents.</p>
<div class="btn-outline abs" style="left:416px;top:321px;width:155px">FIND TALLENT</div>
<div class="btn-outline abs" style="left:610px;top:321px;width:174px">FIND TALLENT</div>
<div class="btn-fill abs" style="left:515px;top:372px;width:168px;height:44px">AREAS OF EXPERTISE</div>
<div class="scroll-down abs">
  <svg width="30" height="30" viewBox="0 0 30 30"><circle cx="15" cy="15" r="14" fill="#3d5ed1"/><path d="M15 8v12M9 15l6 6 6-6" stroke="#fff" stroke-width="3" fill="none" stroke-linecap="round"/></svg>
</div>

<h2 class="section-title abs" style="top:726px">AREAS OF EXPERTISE</h2>

<div class="card abs" style="left:135px;top:834px"><div class="card-photo abs" role="img" aria-label="Team meeting at a whiteboard"></div><div class="card-band abs">SALES AND MARKETING</div><div class="card-body abs"><div class="card-btn abs">LEARN MORE...</div></div></div>
<div class="card abs" style="left:375px;top:834px"><div class="card-photo abs" role="img" aria-label="Presenter addressing a team"></div><div class="card-band abs">SALES FORCE EXPANSION</div><div class="card-body abs"><div class="card-btn abs">LEARN MORE...</div></div></div>
<div class="card abs" style="left:615px;top:834px"><div class="card-photo abs" role="img" aria-label="Hands reviewing documents at a desk"></div><div class="card-band abs">EXECUTIVE LEVEL MANAGEMENT</div><div class="card-body abs"><div class="card-btn abs">LEARN MORE...</div></div></div>
<div class="card abs" style="left:855px;top:834px"><div class="card-photo abs" role="img" aria-label="Professionals shaking hands"></div><div class="card-band abs">PHARMASUTICALS</div><div class="card-body abs"><div class="card-btn abs">LEARN MORE...</div></div></div>

<div class="card abs" style="left:135px;top:1132px"><div class="card-photo abs" role="img" aria-label="Team meeting at a whiteboard"></div><div class="card-band abs">SALES AND MARKETING</div><div class="card-body abs"><div class="card-btn abs">LEARN MORE...</div></div></div>
<div class="card abs" style="left:375px;top:1132px"><div class="card-photo abs" role="img" aria-label="Presenter addressing a team"></div><div class="card-band abs">SALES FORCE EXPANSION</div><div class="card-body abs"><div class="card-btn abs">LEARN MORE...</div></div></div>
<div class="card abs" style="left:615px;top:1132px"><div class="card-photo abs" role="img" aria-label="Hands reviewing documents at a desk"></div><div class="card-band abs">EXECUTIVE LEVEL MANAGEMENT</div><div class="card-body abs"><div class="card-btn abs">LEARN MORE...</div></div></div>
<div class="card abs" style="left:855px;top:1132px"><div class="card-photo abs" role="img" aria-label="Professionals shaking hands"></div><div class="card-band abs">PHARMASUTICALS</div><div class="card-body abs"><div class="card-btn abs">LEARN MORE...</div></div></div>

<h2 class="section-title abs" style="top:1480px">ABOUT US</h2>
<div class="about-photo abs" role="img" aria-label="Team gathered around a meeting table with laptops"></div>
<div class="about-text abs">
  <p><span class="drop-cap">L</span>antern Talent Group is dedicated to, and focused on, helping you secure the most talented people in the market. We assess, recruit, develop and engage the best and brightest people for our corporate clients. Our goal is to improve performance at every level within our client companies so that the whole becomes greater than the sum of each individual’s expertise.</p>
  <p>Our recruiters have over 75 years of combined recruiting expertise in a wide variety of industries ranging from Sales and Marketing to Clinical Research. This collective industry experience has, over the years, produced invaluable contacts with industry leaders and decision makers across all the business arenas we serve.</p>
</div>
<div class="read-more abs">READ MORE...</div>

<section class="cta-band abs" role="img" aria-label="Business handshake in a bright office"></section>
<div class="cta-btn abs" style="left:15px;width:538px">FIND JOBS</div>
<div class="cta-icon abs"><svg width="22" height="20" viewBox="0 0 22 20"><rect x="1" y="1" width="20" height="18" rx="2" fill="none" stroke="#fff" stroke-width="2"/><path d="M3 16l5-6 4 4 3-3 4 5z" fill="#fff"/><circle cx="15" cy="6" r="2" fill="#fff"/></svg></div>
<div class="cta-btn abs" style="left:602px;width:580px">FIND A TALLENT</div>

<footer class="site-footer abs">
  <div class="f-col abs" style="left:52px">
    <h3 class="f-head">CONTACT US</h3>
    <div class="contact-lines">
      <div>248 W. Harbor Ave.</div><div class="gap"></div>
      <div>Riverton, FL 33720</div><div class="gap"></div>
      <div><em>Phone:</em> 555-014-2290</div>
      <div><em>Email:</em> info@lanterntalent.com</div>
    </div>
    <div class="footer-brand"><span class="brand-dot"></span><span class="brand-name">Lantern</span></div>
  </div>
  <div class="f-col abs" style="left:333px">
    <h3 class="f-head">FEATURED CANDIDATE</h3>
    <div class="abs" style="left:0;top:75px;width:260px;height:260px">
      <div class="cand-photo abs" role="img" aria-label="Portrait of the featured candidate"></div>
      <div class="cand-name abs">Test<br>Candidate</div>
      <div class="cand-role abs">Designer Developer</div>
      <div class="cand-info abs">
        <div><svg width="12" height="10" viewBox="0 0 12 10"><rect x=".5" y=".5" width="11" height="9" fill="none" stroke="#fff"/><path d="M.5 .5l5.5 5 5.5-5" fill="none" stroke="#fff"/></svg><span>test@mywebsite.com</span></div>
        <div><svg width="12" height="12" viewBox="0 0 12 12"><path d="M2 1l3 3-1.5 1.5a7 7 0 003 3L8 7l3 3-2 2C5 12 0 7 0 3z" fill="none" stroke="#fff"/></svg><span>(123) 9988 44 77<br>66</span></div>
        <div><svg width="12" height="12" viewBox="0 0 12 12"><path d="M5 7l2-2M4 5L2.5 6.5a2 2 0 003 3L7 8M8 7l1.5-1.5a2 2 0 00-3-3L5 4" fill="none" stroke="#fff"/></svg><span>mywebsite.com</span></div>
        <div><svg width="12" height="14" viewBox="0 0 12 14"><path d="M6 13S1 8 1 5a5 5 0 0110 0c0 3-5 8-5 8z" fill="none" stroke="#fff"/><circle cx="6" cy="5" r="1.6" fill="#fff"/></svg><span>My home<br>My address<br>My city</span></div>
      </div>
    </div>
  </div>
  <div class="f-col abs" style="left:615px">
    <h3 class="f-head">AREAS OF EXPERTISE</h3>
    <ul class="f-list">
      <li>Therapeutic Areas</li><li>Healthcare Marketing</li><li>Biotech</li><li>Medical Devise</li><li>Pharmasuticals</li><li>Executive Level Management</li><li>Sales Force Expansion</li><li>Sales And Marketing</li>
    </ul>
  </div>
  <div class="f-col abs" style="left:896px">
    <h3 class="f-head">MENU</h3>
    <ul class="f-list" style="padding-left:42px">
      <li>HOME</li><li>ABOUT US</li><li>FAQ</li><li>GUARENTEE</li><li>SUBMIT RESUME</li><li>TESTIMONIALS</li>
    </ul>
  </div>
</footer>

<div class="credit-bar abs"><span>Proudly powered by PressCraft</span>&nbsp;| Theme: LanternTheme (Version: 1.0)</div>

</body>
</html>
```